BrivoMatex. Lantern for the Steady Growth. Business card

Professional business card for BrivoMatex (Lantern for the Steady Growth)
My rationale: Strategy-> Execution-> Results-> Value that lead to the BrivoMatex name: We put the Lantern for the Steady Growth.
We deliver value to our customers helping them at defining a good strategy (cyan arrow). 90% of well formulated strategies fail due to poor execution so we also consider strategical execution very important (green arrow). Due to the execution we obtain the results (blue arrow). Finally, the results provide feedback to redefine strategy, and the new strategy has to be executed and new results obtained providing new feedback and on and on. It's like a wheel that finally, must create corporate value: value for shareholders, staholders, employees, providers...-

Target Market(s)

CEOs and steering comitees , invewrnent funds

Industry/Entity Type

Business Consultant

Contact Information for Business Card

Tommaso Ferlini
CEO & Founder
tommaso.ferlini@brivomatex.example
Mobile: +34 611.205.938
www.brivomatex.example

Colors

Designer to choose colors to be used in the design.

Requirements
Nice to have
• Nice to hace the words: Strategy, execution, results
• Nice to vave the claim: Lantern for the Steady Growth
• The three colors should be shown:
• cyan for STRATEGY
• green for EXECUTION
• blue for RESULTS
Should not have
• Complete black background

```html
<!DOCTYPE html>
<html lang="en">
<head>
<meta charset="utf-8">
<title>BrivoMatex – Business Card</title>
<link rel="stylesheet" href="https://fonts.googleapis.com/css2?family=Montserrat:wght@400;500;800&family=Oswald:wght@600&display=swap">
<style>
  :root {
    --stage: #3b3d40;
    --paper: #ffffff;
    --paper-shade: #ececec;
    --brand-blue: #0a33a6;
    --brand-blue-deep: #022487;
    --cyan: #1b9fd9;
    --green: #9bbb4a;
    --ink: #3a3a3a;
    --ink-soft: #5a5a5a;
    --logo-light: #d9dee6;
  }
  * { box-sizing: border-box; margin: 0; padding: 0; }
  html, body { width: 1200px; height: 900px; overflow: hidden; }
  body {
    background: var(--stage);
    display: flex;
    flex-direction: column;
    align-items: center;
    justify-content: center;
    gap: 40px;
    font-family: "Montserrat", Arial, sans-serif;
  }
  .card {
    width: 700px;
    height: 400px;
    position: relative;
    box-shadow: 0 10px 30px rgba(0,0,0,.45);
  }
  .card-front {
    background: radial-gradient(ellipse at 55% 45%, var(--paper) 40%, var(--paper-shade) 100%);
    display: flex;
    align-items: center;
    padding-left: 48px;
    padding-right: 48px;
  }
  .identity {
    flex: none;
    text-align: right;
    padding-right: 22px;
    border-right: 2px solid var(--green);
    padding-top: 6px;
    padding-bottom: 6px;
  }
  .person-name {
    font-family: "Oswald", "Arial Narrow", sans-serif;
    font-weight: 600;
    font-size: 30px;
    letter-spacing: .5px;
    color: var(--cyan);
    text-transform: uppercase;
    line-height: 1.1;
  }
  .person-role {
    font-size: 16px;
    color: var(--ink-soft);
    margin-top: 4px;
  }
  .contact-list {
    list-style: none;
    padding-left: 20px;
    margin-top: 78px;
    min-width: 0;
  }
  .contact-item {
    display: flex;
    align-items: center;
    gap: 8px;
    font-size: 15px;
    font-weight: 500;
    color: var(--ink);
    line-height: 1.6;
    white-space: nowrap;
  }
  .contact-icon { width: 14px; height: 14px; flex: none; }
  .card-back {
    background: linear-gradient(135deg, var(--brand-blue) 0%, var(--brand-blue-deep) 100%);
    display: flex;
    align-items: center;
    justify-content: center;
  }
  .brand-name {
    font-weight: 800;
    font-size: 78px;
    color: var(--logo-light);
    letter-spacing: -1px;
  }
</style>
</head>
<body>
  <section class="card card-front" aria-label="Business card front">
    <div class="identity">
      <h1 class="person-name">Tommaso Ferlini</h1>
      <p class="person-role">CEO &amp; Founder</p>
    </div>
    <ul class="contact-list">
      <li class="contact-item">
        <svg class="contact-icon" viewBox="0 0 16 16" aria-hidden="true"><path d="M4 1.5 6 4 5 5.5c.8 2 2.5 3.7 4.5 4.5L11 9l2.5 2-1 2.5C7 13 3 9 2.5 3.5Z" fill="var(--cyan)"/></svg>
        +34 611.205.938
      </li>
      <li class="contact-item">
        <svg class="contact-icon" viewBox="0 0 16 16" aria-hidden="true"><rect x="1.5" y="3.5" width="13" height="9" rx="1" fill="none" stroke="var(--cyan)" stroke-width="1.5"/><path d="M2 4l6 5 6-5" fill="none" stroke="var(--cyan)" stroke-width="1.5"/></svg>
        tommaso.ferlini@brivomatex.example
      </li>
      <li class="contact-item">
        <svg class="contact-icon" viewBox="0 0 16 16" aria-hidden="true"><circle cx="8" cy="8" r="6.5" fill="none" stroke="var(--cyan)" stroke-width="1.4"/><ellipse cx="8" cy="8" rx="2.8" ry="6.5" fill="none" stroke="var(--cyan)" stroke-width="1.2"/><path d="M1.5 8h13M2.5 5h11M2.5 11h11" stroke="var(--cyan)" stroke-width="1.1"/></svg>
        www.brivomatex.example
      </li>
    </ul>
  </section>

  <section class="card card-back" aria-label="Business card back">
    <p class="brand-name">BrivoMatex</p>
  </section>
</body>
</html>
```